Steel Company / Iron Railing Business Card Template

We are a custom steel fabrication company located in Ashcombe, OH. In business since 1979, we recently developed a new logo, and we're looking for a business card design to help display the new logo and our business. The name of the company is Kelbrook Forge Co.. The Office Phone number is (610) 555-0143. We fabricate and install custom "wrought iron" railings on our residential side, we also fabricate and erect structural steel (think cranes and steel beams in buildings) on our commercial side. Looking to get a business card template designed. Something modern, but professional. Clear and easy to read. Front should have all business and employee information including phone number(s), email address, business information, etc. back should spotlight logo.

Industry/Entity Type

Construction / Home Improvement

Contact Information for Business Card

Business information is Kelbrook Forge Co., 48 Dunmore Ave Suite 3305, Ashcombe, OH 19074. Phone number is (610) 555-0143. Website is www.kelbrookforge.example Business card should be for "Tom Pelling" with the job title "Sales & Estimating" but be editable for other employees. Tom's phone number is (610) 555-0178

Colors

Designer to choose colors to be used in the design.

Requirements
Must have
• Modern Feel, Design should be sized for standard business card sizing 3.5" x 2" (88.9mm x 50.8mm)

```html
<!DOCTYPE html>
<html lang="en">
<head>
<meta charset="utf-8">
<title>Kelbrook Forge Co. – Business Card</title>
<link rel="stylesheet" href="https://fonts.googleapis.com/css2?family=Montserrat:wght@300;400;500;700&display=swap">
<style>
  :root {
    --bg: #d6d6d6;
    --violet: #6b3496;
    --magenta: #c01c6e;
    --crimson: #d21f3c;
    --arc-top: #7e3585;
    --arc-bottom: #b31c7c;
    --royal: #3f68b8;
    --accent: #f1b21c;
    --icon-ink: #8a2a6a;
    --ink: #ffffff;
    --arch: path('M0,200 A200,200 0 0 1 400,200 L400,672 Q400,700 372,700 L28,700 Q0,700 0,672 Z');
  }
  * { box-sizing: border-box; margin: 0; padding: 0; }
  html, body { width: 1200px; height: 1200px; overflow: hidden; }
  body {
    background: var(--bg);
    font-family: 'Montserrat', sans-serif;
    color: var(--ink);
    position: relative;
  }
  .card {
    position: absolute;
    top: 250px;
    width: 400px;
    height: 700px;
    clip-path: var(--arch);
    overflow: hidden;
  }
  .card--front {
    left: 150px;
    background: linear-gradient(65deg, var(--violet) 0%, var(--magenta) 50%, var(--crimson) 100%);
  }
  .card--back { left: 650px; background: var(--royal); }

  .arc { position: absolute; border-radius: 50%; }
  .arc--top {
    width: 520px; height: 520px; left: 140px; top: -230px;
    background: var(--arc-top); opacity: .85;
  }
  .arc--bottom {
    width: 560px; height: 560px; left: 40px; top: 460px;
    background: linear-gradient(90deg, var(--arc-bottom), var(--violet));
    opacity: .75;
  }

  .identity { position: absolute; left: 46px; top: 300px; }
  .identity__name {
    font-weight: 500; font-size: 56px; line-height: 1; letter-spacing: 1px;
  }
  .identity__title { font-weight: 300; font-size: 19px; margin-top: 8px; letter-spacing: .5px; }

  .contact { position: absolute; left: 46px; top: 470px; list-style: none; }
  .contact__item {
    display: flex; align-items: flex-start; gap: 14px;
    font-size: 19px; font-weight: 400; line-height: 1.25; margin-bottom: 14px;
  }
  .contact__item--tight { margin-bottom: 2px; }
  .contact__icon { flex: none; width: 20px; height: 20px; margin-top: 2px; }

  .brand {
    position: absolute; inset: 0;
    display: flex; flex-direction: column; align-items: center; justify-content: center;
    gap: 26px; padding-top: 60px;
  }
  .brand__mark { width: 120px; height: 120px; border-radius: 50%; border: 6px solid var(--ink); }
  .brand__name { font-weight: 700; font-size: 32px; letter-spacing: 1px; text-align: center; line-height: 1.2; }
</style>
</head>
<body>

  <section class="card card--front" aria-label="Business card front">
    <div class="arc arc--top"></div>
    <div class="arc arc--bottom"></div>

    <div class="identity">
      <h1 class="identity__name">Tom<br>Pelling</h1>
      <p class="identity__title">Sales &amp; Estimating</p>
    </div>

    <ul class="contact">
      <li class="contact__item">
        <svg class="contact__icon" viewBox="0 0 20 20" aria-hidden="true">
          <circle cx="10" cy="10" r="10" fill="var(--accent)"/>
          <rect x="7" y="5" width="6" height="10" rx="1.5" fill="none" stroke="var(--icon-ink)" stroke-width="1.6"/>
        </svg>
        <span>(610) 555-0178</span>
      </li>
      <li class="contact__item">
        <svg class="contact__icon" viewBox="0 0 20 20" aria-hidden="true">
          <circle cx="10" cy="10" r="10" fill="var(--accent)"/>
          <path d="M10 4.5a3.5 3.5 0 0 0-3.5 3.5c0 2.6 3.5 7 3.5 7s3.5-4.4 3.5-7A3.5 3.5 0 0 0 10 4.5z" fill="var(--icon-ink)"/>
          <circle cx="10" cy="8" r="1.3" fill="var(--accent)"/>
        </svg>
        <span>48 Dunmore Ave Suite 3305,<br>Ashcombe, OH 19074.</span>
      </li>
      <li class="contact__item contact__item--tight">
        <svg class="contact__icon" viewBox="0 0 20 20" aria-hidden="true">
          <circle cx="10" cy="10" r="10" fill="var(--accent)"/>
          <rect x="5" y="6.5" width="10" height="7" rx="1" fill="none" stroke="var(--icon-ink)" stroke-width="1.6"/>
        </svg>
        <span>(610) 555-0143</span>
      </li>
      <li class="contact__item">
        <svg class="contact__icon" viewBox="0 0 20 20" aria-hidden="true">
          <circle cx="10" cy="10" r="10" fill="var(--accent)"/>
          <circle cx="10" cy="10" r="5" fill="none" stroke="var(--icon-ink)" stroke-width="1.4"/>
          <path d="M5 10h10M10 5c-2.4 2.8-2.4 7.2 0 10M10 5c2.4 2.8 2.4 7.2 0 10" fill="none" stroke="var(--icon-ink)" stroke-width="1.2"/>
        </svg>
        <span>www.kelbrookforge.example</span>
      </li>
    </ul>
  </section>

  <section class="card card--back" aria-label="Business card back">
    <div class="brand">
      <div class="brand__mark"></div>
      <p class="brand__name">Kelbrook<br>Forge Co.</p>
    </div>
  </section>

</body>
</html>
```